We need a poster design for "KEVO Sports Night" events. The events have been around for 3 years and we hope the poster will give a sense of vibrant and active designs. It is more to a community event with teamwork and fun.

I have uploaded a past event poster just FYI.

Target Market(s)

Community, Family

Industry/Entity Type

Non Profit

Logo Text

KEVO Sports Night

Requirements
Must have
• KEVO Sports Night
• Organiser: KEVO Sydney
• Date: 25/11/2017
• Time: 4:00pm
• Venue: Wendamere Park
• Facebook: kevosport

```html
<!DOCTYPE html>
<html lang="en">
<head>
<meta charset="utf-8">
<title>KEVO Sports Night</title>
<link rel="stylesheet" href="https://fonts.googleapis.com/css2?family=Bebas+Neue&family=Oswald:wght@400&family=Montserrat:wght@400;600;700&display=swap">
<style>
  :root {
    --page: #ffffff;
    --poster: #000000;
    --ink: #ffffff;
    --accent: #f25a22;
    --paint-yellow: #f0e21c;
    --paint-amber: #f5a31b;
    --paint-orange: #f0701f;
    --paint-red: #e6302b;
    --paint-umber: #9a4a12;
  }
  html, body {
    margin: 0;
    width: 1200px;
    height: 900px;
    overflow: hidden;
    background: var(--page);
  }
  .poster {
    position: absolute;
    left: 334px;
    top: 76px;
    width: 526px;
    height: 744px;
    background: var(--poster);
    overflow: hidden;
  }
  .title {
    position: absolute;
    left: 0;
    top: 0;
    width: 526px;
    height: 640px;
  }
  .title text {
    font-family: "Bebas Neue", "Oswald", sans-serif;
  }
  .time-badge {
    position: absolute;
    left: 46px;
    top: 641px;
    width: 220px;
    height: 83px;
    background: var(--accent);
    color: var(--ink);
    display: flex;
    align-items: center;
    justify-content: center;
    font-family: "Oswald", sans-serif;
    font-size: 72px;
    line-height: 1;
    letter-spacing: 2px;
  }
  .time-badge .meridiem {
    font-size: 32px;
    align-self: flex-start;
    margin-top: 12px;
    margin-left: 4px;
  }
  .details {
    position: absolute;
    left: 285px;
    top: 640px;
    width: 214px;
    color: var(--ink);
    font-family: "Montserrat", sans-serif;
  }
  .details p { margin: 0; white-space: nowrap; }
  .details .date {
    font-size: 25px;
    font-weight: 600;
    letter-spacing: 3.5px;
  }
  .details .venue {
    font-size: 14px;
    margin-top: 6px;
  }
  .details .venue strong { font-weight: 700; }
  .details .organiser {
    font-size: 13px;
    font-weight: 600;
    letter-spacing: 0.6px;
    margin-top: 10px;
  }
  .details .social {
    font-size: 13px;
    font-weight: 600;
    letter-spacing: 0.6px;
    margin-top: 2px;
  }
</style>
</head>
<body>
  <main class="poster">
    <svg class="title" viewBox="0 0 526 640" role="img" aria-label="KEVO Sports Night, lettering filled with vibrant yellow, orange and red watercolour paint texture with a runner photo">
      <defs>
        <linearGradient id="paint-fill" gradientUnits="userSpaceOnUse" x1="20" y1="40" x2="520" y2="620">
          <stop offset="0" stop-color="var(--paint-yellow)"/>
          <stop offset="0.35" stop-color="var(--paint-amber)"/>
          <stop offset="0.65" stop-color="var(--paint-orange)"/>
          <stop offset="1" stop-color="var(--paint-red)"/>
        </linearGradient>
        <linearGradient id="paint-shade" gradientUnits="userSpaceOnUse" x1="40" y1="440" x2="300" y2="640">
          <stop offset="0" stop-color="var(--paint-umber)" stop-opacity="0.75"/>
          <stop offset="1" stop-color="var(--paint-umber)" stop-opacity="0"/>
        </linearGradient>
      </defs>
      <g fill="url(#paint-fill)">
        <text x="41" y="269" font-size="344" textLength="458" lengthAdjust="spacingAndGlyphs">KEVO</text>
        <text x="41" y="422" font-size="190" textLength="458" lengthAdjust="spacingAndGlyphs">SPORTS</text>
        <text x="41" y="624" font-size="250" textLength="458" lengthAdjust="spacingAndGlyphs">NIGHT</text>
      </g>
      <text x="41" y="624" font-size="250" textLength="458" lengthAdjust="spacingAndGlyphs" fill="url(#paint-shade)">NIGHT</text>
    </svg>

    <div class="time-badge">4:00<span class="meridiem">PM</span></div>

    <div class="details">
      <p class="date">25 | 11 | 2017</p>
      <p class="venue">VENUE <strong>WENDAMERE PARK</strong></p>
      <p class="organiser">ORGANIZED BY KEVO SYDNEY</p>
      <p class="social">FB.COM/KEVOSPORT</p>
    </div>
  </main>
</body>
</html>
```